" A empresa em questao será uma clínica médica e de fisioterapia especializada em tratamento de coluna. Tanto os médicos quanto os tratamentos fisioterápicos (fisioterapia, osteopatia, RPG) serao direcionados para o público que busca tratamento e soluçoes para dores nas costas em geral. "

```html
<!DOCTYPE html>
<html lang="pt-BR">
<head>
<meta charset="UTF-8">
<title>Instituto Eixo Leve — Cartão de Visita</title>
<link rel="stylesheet" href="https://fonts.googleapis.com/css2?family=Open+Sans:wght@300;400&display=swap">
<style>
  :root {
    --canvas: #ececea;
    --card-black: #0b0b0b;
    --card-white: #ffffff;
    --ink-light: #f2f2f2;
    --ink-grey: #b9b9b9;
    --accent-teal: #5cc3cd;
    --shadow: rgba(0, 0, 0, 0.18);
  }
  * { margin: 0; padding: 0; box-sizing: border-box; }
  html, body {
    width: 1200px;
    height: 1200px;
    overflow: hidden;
    background: var(--canvas);
    font-family: "Open Sans", Arial, sans-serif;
  }
  .stage {
    position: relative;
    width: 1200px;
    height: 1200px;
  }
  .card {
    position: absolute;
    left: 220px;
    width: 760px;
    height: 440px;
    border-radius: 56px;
    overflow: hidden;
    box-shadow: 0 14px 30px var(--shadow);
  }
  /* Front */
  .card-front {
    top: 130px;
    background: var(--card-black);
  }
  .brand-lockup {
    position: absolute;
    left: 190px;
    top: 148px;
    display: flex;
    align-items: center;
  }
  .brand-dot {
    width: 96px;
    height: 96px;
    border-radius: 50%;
    background: var(--accent-teal);
    margin-right: 40px;
  }
  .brand-divider {
    width: 2px;
    height: 140px;
    background: var(--ink-light);
    margin-right: 18px;
  }
  .brand-name {
    color: var(--ink-light);
    font-weight: 300;
    line-height: 1.05;
  }
  .brand-name .kicker { display: block; font-size: 30px; letter-spacing: 0.5px; }
  .brand-name .main { display: block; font-size: 46px; }

  /* Back */
  .card-back {
    top: 650px;
    background: var(--card-black);
  }
  .back-left {
    position: absolute;
    left: 0;
    top: 0;
    width: 290px;
    height: 100%;
    background: var(--card-white);
    display: flex;
    flex-direction: column;
    justify-content: center;
    padding-left: 44px;
  }
  .back-brand {
    color: var(--ink-grey);
    font-weight: 300;
    line-height: 1.05;
  }
  .back-brand .kicker { display: block; font-size: 24px; }
  .back-brand .main { display: block; font-size: 40px; }
  .contact {
    position: absolute;
    right: 56px;
    text-align: right;
    color: var(--ink-light);
    font-weight: 400;
  }
  .contact-person { top: 52px; font-size: 25px; line-height: 1.45; }
  .contact-lines { top: 160px; font-size: 24px; line-height: 1.5; }
  .contact-address { top: 322px; font-size: 15px; line-height: 1.45; }
</style>
</head>
<body>
<main class="stage">
  <section class="card card-front" aria-label="Frente do cartão">
    <div class="brand-lockup">
      <span class="brand-dot" aria-hidden="true"></span>
      <span class="brand-divider" aria-hidden="true"></span>
      <p class="brand-name">
        <span class="kicker">instituto</span>
        <span class="main">Eixo</span>
        <span class="main">Leve</span>
      </p>
    </div>
  </section>

  <section class="card card-back" aria-label="Verso do cartão">
    <div class="back-left">
      <p class="back-brand">
        <span class="kicker">instituto</span>
        <span class="main">Eixo Leve</span>
      </p>
    </div>
    <div class="contact contact-person">
      <p>Nome Sobrenome</p>
      <p>Função</p>
    </div>
    <div class="contact contact-lines">
      <p>(00)0000-0000</p>
      <p>contato@contato.com.br</p>
    </div>
    <div class="contact contact-address">
      <p>Rua Sem Nome,00</p>
      <p>Bairro Sem Nome</p>
      <p>Cidade Sem Nome</p>
    </div>
  </section>
</main>
</body>
</html>
```